Paws About Town Helpers

Design a flyer (A5 - I think!) with bright colours to promote an in home Dog Service.
Include an animated picture of a dog (being walked/playing/jumping etc)
Bold Heading, list of services with animated pictures, contact details

Industry/Entity Type

It Service

Requirements
Must have
• Add price list to back of A5 Flyer with same colours and design as front page of flyer - See Attached.

```html
<!DOCTYPE html>
<html lang="en">
<head>
<meta charset="UTF-8">
<title>Paws About Town Helpers – Dog Service Flyer</title>
<link rel="stylesheet" href="https://fonts.googleapis.com/css2?family=Fredoka+One&family=Fredoka:wght@600&display=swap">
<style>
  :root {
    --brand-red: #c1272d;
    --ink: #111111;
    --paper: #ffffff;
    --illustration-light: #f1efee;
    --illustration-mid: #d9d5d3;
  }
  * { margin: 0; padding: 0; box-sizing: border-box; }
  html, body { width: 852px; height: 1200px; overflow: hidden; background: var(--paper); }
  .flyer {
    position: relative;
    width: 852px;
    height: 1200px;
    background: var(--paper);
    font-family: "Fredoka One", "Fredoka", sans-serif;
    color: var(--ink);
    overflow: hidden;
  }
  .headline-band {
    position: absolute; left: 0; top: 0;
    width: 852px; height: 280px;
    background: var(--brand-red);
    color: var(--paper);
    text-align: center;
  }
  .headline-kicker {
    position: absolute; left: 0; right: 0; top: 30px;
    font-size: 66px; line-height: 1; letter-spacing: 1px;
  }
  .headline-main {
    position: absolute; left: 0; right: 0; top: 118px;
    font-size: 128px; line-height: 1; letter-spacing: 2px;
  }
  .tagline {
    position: absolute; left: 0; right: 0; top: 302px;
    text-align: center;
    font-size: 41px; line-height: 1.1;
  }
  .tagline-brand {
    position: absolute; left: 0; right: 0; top: 362px;
    text-align: center;
    font-size: 33px; line-height: 1.1;
    color: var(--brand-red);
  }
  .services {
    position: absolute; left: 48px; top: 456px;
    width: 470px;
    list-style: none;
  }
  .service { margin-bottom: 30px; }
  .service-question {
    font-size: 19.5px; line-height: 28px;
    text-transform: uppercase;
    letter-spacing: 0.3px;
  }
  .service-answer {
    font-family: "Fredoka", sans-serif; font-weight: 600;
    margin-left: 58px;
    font-size: 20.5px; line-height: 29px;
    color: var(--brand-red);
  }
  .dog-illustration {
    position: absolute; left: 510px; top: 410px;
    width: 342px; height: 575px;
    background: radial-gradient(ellipse at 55% 45%, var(--illustration-light) 0%, var(--illustration-mid) 100%);
    border-radius: 140px 0 0 0;
  }
  .contact-band {
    position: absolute; left: 0; top: 985px;
    width: 852px; height: 113px;
    background: var(--brand-red);
    color: var(--paper);
    text-align: center;
    font-size: 82px; line-height: 113px;
    letter-spacing: 1px;
  }
  .website {
    position: absolute; left: 0; right: 0; top: 1110px;
    text-align: center;
    font-size: 47px; line-height: 1.3;
  }
</style>
</head>
<body>
  <main class="flyer">
    <header class="headline-band">
      <div class="headline-kicker">TIRED OF PICKING UP</div>
      <h1 class="headline-main">DOG POOP?</h1>
    </header>

    <p class="tagline">Arrange for us to do it for you!</p>
    <p class="tagline-brand">We are PAWS ABOUT TOWN HELPERS!</p>

    <ul class="services">
      <li class="service">
        <div class="service-question">Need a break from<br>walking the dog?</div>
        <div class="service-answer">We will come and collect your<br>dog and take it for a walk!</div>
      </li>
      <li class="service">
        <div class="service-question">Can’t get home in time<br>to feed your dog?</div>
        <div class="service-answer">Use our dog feeding service!</div>
      </li>
      <li class="service">
        <div class="service-question">Want someone to play with your<br>dog while you’re at work?</div>
        <div class="service-answer">We will be Paws About Town<br>Helpers!</div>
      </li>
      <li class="service">
        <div class="service-question">Dog needs a bath?</div>
        <div class="service-answer">We’ll arrange for a professional<br>to keep it clean!</div>
      </li>
    </ul>

    <div class="dog-illustration" role="img" aria-label="Cartoon illustration of a smiling white spotted dog with a red collar"></div>

    <div class="contact-band">Tel: 0491 57 03 48</div>
    <div class="website">www.pawsabouttown.com.au</div>
  </main>
</body>
</html>
```